Lintel Systems

Looking for a web site design to market our services/applications
We write and supply bespoke web applications for the offshore and construction industries
Our initial product is Volk - rope access equipment management
Our buyers will be Rope Access companies via trade associations such as KEFOB and GLUMP
we have a logo designed see it attached we would like to see crisp professional designs based around these colours and design
we will supply web copy later
looking for home, services, blog, contact us, order and a general template (privacy, site map, T&C) pages
Updates
This payment will be for the homepage only
We can discuss other options (pages) with the successful designer
Regards
Norman
Industry/Entity Type
Construction
Look and feel

```html
<!DOCTYPE html>
<html lang="en">
<head>
<meta charset="utf-8">
<title>Lintel Systems</title>
<link href="https://fonts.googleapis.com/css2?family=Open+Sans:wght@400;600;700&display=swap" rel="stylesheet">
<style>
:root{
  --blue:#1a8fd6;
  --blue-dark:#0d6eb0;
  --navy:#1b3a5c;
  --ink:#2b2b2b;
  --muted:#8a8a8a;
  --panel:#e9e9e9;
  --footer:#2e2e2e;
  --white:#ffffff;
}
*{box-sizing:border-box;margin:0;padding:0}
html,body{width:778px;height:1200px;overflow:hidden}
body{font-family:"Open Sans",Arial,sans-serif;color:var(--ink);background:var(--white)}
.site-header{height:90px;display:flex;align-items:center;justify-content:space-between;padding:0 40px 0 115px}
.brand{display:flex;align-items:center;gap:10px}
.brand-mark{width:34px;height:34px;background:var(--blue)}
.brand-name{font-size:20px;font-weight:700;color:var(--navy);line-height:1.05;width:120px}
.phone{font-size:15px;font-weight:600;color:var(--navy)}
.main-nav{height:32px;background:linear-gradient(var(--blue),var(--blue-dark));padding:0 115px;display:flex;gap:28px;align-items:center}
.main-nav a{color:var(--white);font-size:11px;font-weight:600;text-decoration:none}
.hero{position:relative;height:268px;background:linear-gradient(100deg,#6d7a86 0%,#c9936a 45%,#f2b27a 60%,#b66a3d 100%)}
.hero-copy{position:absolute;left:115px;top:60px;width:300px}
.hero-title{font-size:34px;font-weight:700;color:var(--white);line-height:1.1}
.hero-sub{margin-top:12px;font-size:11px;color:var(--white);line-height:1.45}
.hero-dots{position:absolute;right:120px;bottom:14px;display:flex;gap:7px}
.hero-dots span{width:8px;height:8px;border-radius:50%;background:rgba(255,255,255,.55)}
.hero-dots span:first-child{background:var(--white)}
.welcome{padding:32px 115px 0}
.welcome h1{text-align:center;font-size:22px;font-weight:700;color:var(--blue);margin-bottom:28px}
.welcome-body{display:flex;gap:30px}
.welcome-text{width:320px}
.lead{font-size:13px;font-weight:600;line-height:1.45;margin-bottom:12px}
.welcome-text p.body{font-size:10.5px;color:var(--muted);line-height:1.6}
.btn{display:inline-block;margin-top:26px;background:var(--blue);color:var(--white);font-size:12px;font-weight:600;padding:13px 18px}
.tiles{display:grid;grid-template-columns:110px 110px;gap:8px}
.tile{height:84px}
.tile-dark{background:#3a3a3a;padding:8px;color:var(--white)}
.tile-dark h3{font-size:10px;font-weight:700;line-height:1.3}
.tile-dark p{font-size:8px;color:#c7c7c7;margin-top:4px;line-height:1.4}
.photo-a{background:linear-gradient(#4d6f94,#2c3f57)}
.photo-b{background:linear-gradient(#7fa8c9,#3d5f7a)}
.photo-c{background:linear-gradient(#5b87b5,#284766)}
.services{padding:48px 115px 0}
.services h2{font-size:17px;font-weight:600;margin-bottom:16px}
.service-row{display:flex;justify-content:space-between}
.service{width:160px;text-align:center}
.service-icon{width:64px;height:64px;border-radius:50%;background:var(--blue);margin:0 auto 12px;display:flex;align-items:center;justify-content:center}
.service h3{font-size:11px;font-weight:700;margin-bottom:8px}
.service p{font-size:9px;color:var(--muted);line-height:1.55}
.bottom-panels{display:flex;gap:16px;padding:40px 115px 0}
.panel{background:var(--panel);height:122px;padding:12px 16px}
.testimonials{width:300px}
.buyers{width:232px}
.panel h2{font-size:14px;font-weight:600;margin-bottom:10px}
.quote{font-size:9px;color:var(--muted);line-height:1.55;padding-left:24px;position:relative}
.quote::before{content:"\201C";position:absolute;left:0;top:-6px;font-size:28px;color:#b9b9b9}
.author{text-align:right;font-size:9px;font-weight:600;margin-top:6px}
.badges{display:flex;gap:14px}
.badge{width:92px;height:60px;background:var(--white);border-radius:50%/50%}
.badge.square{border-radius:4px;background:#d7d7d7}
.site-footer{position:absolute;left:0;top:1120px;width:778px;height:80px;background:var(--footer);padding:18px 115px}
.footer-nav{display:flex;gap:22px}
.footer-nav a{color:var(--white);font-size:9.5px;text-decoration:none}
.copyright{margin-top:12px;font-size:9px;color:#bdbdbd}
</style>
</head>
<body>
<header class="site-header">
  <div class="brand"><span class="brand-mark"></span><span class="brand-name">Lintel Systems</span></div>
  <div class="phone">Call us: 1800-555-0142</div>
</header>
<nav class="main-nav">
  <a href="#">HOME</a><a href="#">SERVICES</a><a href="#">BLOG</a><a href="#">ORDER</a><a href="#">CONTACT US</a>
</nav>
<section class="hero" role="img" aria-label="Construction site with cranes and buildings at sunset">
  <div class="hero-copy">
    <div class="hero-title">Web applications for Construction</div>
    <p class="hero-sub">Tailored software for crews and sites, managing equipment, inspections and records from one simple dashboard online.</p>
  </div>
  <div class="hero-dots"><span></span><span></span><span></span></div>
</section>
<section class="welcome">
  <h1>WELCOME TO LINTEL SYSTEMS</h1>
  <div class="welcome-body">
    <div class="welcome-text">
      <p class="lead">We build bespoke web applications for the offshore and construction industries worldwide.</p>
      <p class="body">Our tools help rope access teams track equipment, log inspections and keep certification current. Every project is shaped around how your people work on site, so records stay accurate, audits run smoothly and managers see the full picture at a glance from any device.</p>
      <span class="btn">View Details</span>
    </div>
    <div class="tiles">
      <div class="tile tile-dark"><h3>WIND ENERGY SERVICES</h3><p>Access planning for turbine maintenance crews.</p></div>
      <div class="tile photo-a" role="img" aria-label="City skyline at dusk"></div>
      <div class="tile photo-b" role="img" aria-label="Waterfront buildings"></div>
      <div class="tile photo-c" role="img" aria-label="Harbour at evening"></div>
    </div>
  </div>
</section>
<section class="services">
  <h2>What We Do</h2>
  <div class="service-row">
    <div class="service">
      <div class="service-icon"><svg width="30" height="30" viewBox="0 0 30 30" fill="none" stroke="#fff" stroke-width="2.4"><circle cx="15" cy="15" r="5"/><path d="M15 3v5M15 22v5M3 15h5M22 15h5M6.5 6.5l3.5 3.5M20 20l3.5 3.5M6.5 23.5l3.5-3.5M20 10l3.5-3.5"/></svg></div>
      <h3>VOLK</h3>
      <p>Rope access equipment management with inspection logs and alerts for every item.</p>
    </div>
    <div class="service">
      <div class="service-icon"><svg width="28" height="30" viewBox="0 0 28 30" fill="none" stroke="#fff" stroke-width="2.4"><rect x="4" y="4" width="20" height="24" rx="2"/><path d="M9 12h10M9 17h10M9 22h6"/></svg></div>
      <h3>SERVICES</h3>
      <p>Custom applications built around site workflows, records and team reporting needs.</p>
    </div>
    <div class="service">
      <div class="service-icon"><svg width="30" height="30" viewBox="0 0 30 30" fill="none" stroke="#fff" stroke-width="2.4"><path d="M3 5h4l3 14h14l3-10H9"/><circle cx="12" cy="24" r="2"/><circle cx="22" cy="24" r="2"/></svg></div>
      <h3>ORDER</h3>
      <p>Request a licence or demo online and get your team started within days.</p>
    </div>
  </div>
</section>
<section class="bottom-panels">
  <div class="panel testimonials">
    <h2>Testimonials</h2>
    <p class="quote">Since switching to Volk our inspection records are always complete, and audits take a fraction of the time they used to take.</p>
    <p class="author">Dale Morrow</p>
  </div>
  <div class="panel buyers">
    <h2>Our buyers</h2>
    <div class="badges"><span class="badge"></span><span class="badge square"></span></div>
  </div>
</section>
<footer class="site-footer">
  <nav class="footer-nav"><a href="#">HOME</a><a href="#">SERVICES</a><a href="#">PRIVACY</a><a href="#">SITEMAP</a><a href="#">T&amp;C</a><a href="#">CONTACT US</a></nav>
  <p class="copyright">© 2014 Lintel Systems. All rights reserved.</p>
</footer>
</body>
</html>
```